Business card design for Birch Engineering Torvant

We need a new business card design along with all the necessary to place an order. The company is Birch Engineering Torvant and we recently updated our logo.

```html
<!DOCTYPE html>
<html lang="en">
<head>
<meta charset="utf-8">
<title>Birch Engineering Torvant — Business Card</title>
<link rel="stylesheet" href="https://fonts.googleapis.com/css2?family=Montserrat:wght@400;500;700&display=swap">
<style>
  :root {
    --bg: #e9e9e9;
    --card-grey: #8f8f8f;
    --card-white: #ffffff;
    --brand-yellow: #e2bd1f;
    --ink: #1c1c1c;
    --mark-grey: #8a8a8a;
  }
  * { box-sizing: border-box; margin: 0; padding: 0; }
  html, body { width: 1200px; height: 874px; overflow: hidden; }
  body {
    background: var(--bg);
    font-family: "Montserrat", sans-serif;
    position: relative;
  }
  .card {
    position: absolute;
    left: 260px;
    width: 680px;
    height: 390px;
    border-radius: 26px;
    overflow: hidden;
    box-shadow: 0 6px 18px rgba(0,0,0,.18);
  }
  .card--front { top: 40px; background: var(--card-grey); }
  .card--back { top: 454px; background: var(--card-white); }

  .wordmark {
    display: flex;
    align-items: center;
    gap: 14px;
    font-weight: 700;
    letter-spacing: .04em;
    text-transform: uppercase;
  }
  .wordmark__square { display: block; background: var(--brand-yellow); }

  .card--front .wordmark {
    position: absolute; inset: 0;
    justify-content: center;
    color: #ffffff;
    font-size: 34px;
  }
  .card--front .wordmark__square { width: 26px; height: 26px; }

  .card--back .wordmark {
    position: absolute;
    left: 44px; top: 150px;
    width: 300px;
    color: var(--mark-grey);
    font-size: 20px;
    line-height: 1.3;
  }
  .card--back .wordmark__square { width: 18px; height: 18px; flex: none; }

  .divider {
    position: absolute;
    left: 370px; top: 108px;
    width: 2px; height: 150px;
    background: var(--brand-yellow);
  }
  .contact {
    position: absolute;
    left: 392px; top: 104px;
    color: var(--ink);
  }
  .contact__name { color: var(--brand-yellow); font-weight: 700; font-size: 25px; line-height: 1.1; }
  .contact__role { font-size: 16px; font-weight: 500; margin-bottom: 10px; }
  .contact__address { font-size: 15px; line-height: 1.3; margin-bottom: 10px; }
  .contact__list { list-style: none; font-size: 15px; line-height: 1.55; }
  .contact__list li { display: flex; align-items: center; gap: 9px; }
  .contact__list svg { width: 13px; height: 13px; fill: var(--brand-yellow); flex: none; }

  .base-band { position: absolute; left: 0; bottom: 0; width: 680px; height: 70px; }
</style>
</head>
<body>
  <section class="card card--front" aria-label="Card front">
    <div class="wordmark">
      <span class="wordmark__square"></span>
      <span>Birch Engineering Torvant</span>
    </div>
  </section>

  <section class="card card--back" aria-label="Card back">
    <div class="wordmark">
      <span class="wordmark__square"></span>
      <span>Birch Engineering Torvant</span>
    </div>

    <div class="divider"></div>

    <div class="contact">
      <p class="contact__name">Owen Castell</p>
      <p class="contact__role">Managing Director</p>
      <p class="contact__address">42 Summit Ridge Road<br>Lakeford, NJ 07410 USA</p>
      <ul class="contact__list">
        <li><svg viewBox="0 0 24 24"><path d="M6.6 10.8a15.1 15.1 0 0 0 6.6 6.6l2.2-2.2a1 1 0 0 1 1-.25 11.4 11.4 0 0 0 3.6.57 1 1 0 0 1 1 1V20a1 1 0 0 1-1 1A17 17 0 0 1 3 4a1 1 0 0 1 1-1h3.5a1 1 0 0 1 1 1c0 1.25.2 2.45.57 3.57a1 1 0 0 1-.25 1z"/></svg>(555)214-7730</li>
        <li><svg viewBox="0 0 24 24"><path d="M2 5h20v14H2z M2 5l10 8 10-8" /></svg>info@birchtorvant.com</li>
        <li><svg viewBox="0 0 24 24"><circle cx="12" cy="12" r="10"/></svg>www.birchtorvant.com</li>
      </ul>
    </div>

    <svg class="base-band" viewBox="0 0 680 70" preserveAspectRatio="none" aria-hidden="true">
      <polygon points="0,0 310,40 290,70 0,70" fill="#8f8f8f"/>
      <polygon points="322,42 680,88 680,70 302,70" fill="#e2bd1f"/>
      <polygon points="322,42 680,55 680,70 302,70" fill="#e2bd1f"/>
    </svg>
  </section>
</body>
</html>
```